Maple Junction: PowerPoint Design Project

I'm looking for a PowerPoint design that my real estate ompany will use for business proposals and presentations.
Updates

Project Deadline Extended
Reason: I'm making the contest "guaranteed payment" as requested by some designers. I'll be using the PowerPoint slides for client presentations. The tag lines given can be a footer or watermark because it just give an idea of what we do and what our company values are.

Target Market(s)

Landlords and corporate companies

Industry/Entity Type

Real Estate

Requirements
Must have
• Company logo
Various Tag lines as a part of the design of the PowerPoint:
1st tagline: we don't just build your business, we build your community
2nd tag line: we excel in generating revenue, enhancing the guest experience and protecting the brand.
3rd tag line: we are all about people, projects and profits

```html
<!DOCTYPE html>
<html lang="en">
<head>
<meta charset="utf-8">
<title>Maple Junction Property Consultants – Presentation Template</title>
<link rel="stylesheet" href="https://fonts.googleapis.com/css2?family=Carlito:wght@400;700&family=Fira+Sans+Condensed:wght@600;700&family=Open+Sans:wght@400;600;700&display=swap">
<style>
  :root {
    --bg-dark: #1d1d1d;
    --bg-mid: #2e2e2e;
    --green: #52b13f;
    --green-title: #4aad38;
    --green-deep: #1e6a14;
    --green-bright: #3e9a2e;
    --purple: #5b0fb3;
    --panel: rgba(244, 249, 243, 0.95);
    --ink: #333;
    --page-num: rgba(255, 255, 255, 0.55);
  }
  * { margin: 0; padding: 0; box-sizing: border-box; }
  html, body { width: 960px; height: 1200px; overflow: hidden; }
  body {
    background: radial-gradient(ellipse at 50% 50%, var(--bg-mid) 0%, var(--bg-dark) 75%);
    font-family: "Carlito", "Open Sans", Arial, sans-serif;
  }
  .stage {
    position: relative;
    width: 1200px; height: 1500px;
    transform: scale(0.8);
    transform-origin: 0 0;
  }
  .slide {
    position: absolute;
    left: 290px;
    width: 620px; height: 465px;
    overflow: hidden;
  }
  .slide--cover { top: 29px; background: radial-gradient(ellipse at 55% 45%, #4aa63a 0%, var(--green-bright) 35%, var(--green-deep) 100%); }
  .slide--content-a { top: 519px; }
  .slide--content-b { top: 1009px; }
  .slide--content-a, .slide--content-b {
    background: radial-gradient(ellipse at 50% 45%, #fafafa 0%, #ececec 55%, #d6d6d6 100%);
  }
  .slide svg { position: absolute; left: 0; top: 0; width: 620px; height: 465px; }

  .brand { position: absolute; display: flex; align-items: center; gap: 9px; white-space: nowrap; }
  .brand__mark { width: 32px; height: 32px; border-radius: 50%; background: var(--green); flex: none; }
  .brand__name { font-family: "Fira Sans Condensed", "Carlito", sans-serif; font-weight: 700; color: var(--purple); font-size: 10.5px; line-height: 1.2; }
  .brand__tag { font-family: "Open Sans", Arial, sans-serif; font-size: 5.5px; color: var(--ink); font-weight: 600; margin-top: 2px; }

  .brand--cover { left: 177px; width: 266px; top: 26px; flex-direction: column; gap: 12px; text-align: center; }
  .brand--cover .brand__mark { width: 36px; height: 36px; }
  .brand--cover .brand__name { font-size: 12.5px; }
  .brand--cover .brand__tag { font-size: 6.5px; }
  .brand--right { right: 23px; top: 11px; }
  .brand--left { left: 24px; top: 11px; }

  .cover-line { position: absolute; font-family: "Carlito", sans-serif; font-weight: 700; line-height: 1; white-space: nowrap; }
  .cover-line--lead { left: 198px; top: 181px; font-size: 38px; color: var(--green-title); }
  .cover-line--sub { left: 199px; top: 215px; font-size: 22px; color: var(--purple); }
  .cover-line--big { left: 198px; top: 235px; font-size: 40px; color: var(--green-title); }
  .cover-line--write { left: 357px; top: 241px; font-size: 13px; font-weight: 400; color: var(--green-title); }
  .cover-line--here { left: 357px; top: 258px; font-size: 13px; color: var(--purple); }
  .cover-subtitle { position: absolute; left: 177px; width: 266px; top: 300px; text-align: center; color: var(--purple); font-family: Arial, sans-serif; font-weight: 700; font-size: 12.5px; white-space: nowrap; }

  .tagline { position: absolute; color: #fff; font-size: 10.5px; line-height: 1.3; white-space: nowrap; }
  .tagline--center { left: 0; width: 620px; top: 446px; text-align: center; }
  .tagline--right { right: 20px; top: 432px; text-align: right; }

  .page-no { position: absolute; color: var(--page-num); font-family: "Open Sans", Arial, sans-serif; font-weight: 700; text-align: center; line-height: 1; }
  .page-no__label { display: block; font-size: 8px; font-weight: 400; }
  .page-no__value { display: block; font-size: 38px; }
  .page-no--right { left: 570px; top: 403px; }
  .page-no--left { left: 23px; top: 423px; }
  .page-no--left .page-no__label { font-size: 6px; }
  .page-no--left .page-no__value { font-size: 30px; }
</style>
</head>
<body>
<div class="stage">

  <section class="slide slide--cover">
    <svg viewBox="0 0 620 465" aria-hidden="true">
      <defs>
        <filter id="panel-shadow" x="-20%" y="-20%" width="140%" height="140%">
          <feDropShadow dx="0" dy="3" stdDeviation="5" flood-color="#0b3a06" flood-opacity="0.45"/>
        </filter>
      </defs>
      <path d="M177,0 H443 V365 Q310,470 177,365 Z" fill="var(--panel)" filter="url(#panel-shadow)"/>
    </svg>
    <div class="brand brand--cover">
      <span class="brand__mark"></span>
      <div>
        <div class="brand__name">Maple Junction Property Consultants</div>
        <div class="brand__tag">Experiential Retail And Turn Around Professionals</div>
      </div>
    </div>
    <div class="cover-line cover-line--lead">SAMPLE TEXT</div>
    <div class="cover-line cover-line--sub">FOR LATITUDE TEMPLATE</div>
    <div class="cover-line cover-line--big">YOU CAN</div>
    <div class="cover-line cover-line--write">WRITE</div>
    <div class="cover-line cover-line--here">TITLE HERE</div>
    <div class="cover-subtitle">SUBTITLE GOES HERE</div>
  </section>

  <section class="slide slide--content-a">
    <svg viewBox="0 0 620 465" aria-hidden="true">
      <path d="M0,357 Q330,480 620,335 V465 H0 Z" fill="var(--green)"/>
      <path d="M0,375 Q330,482 620,348 V465 H0 Z" fill="var(--purple)"/>
      <path d="M0,405 Q330,470 620,365 V465 H0 Z" fill="var(--green)"/>
    </svg>
    <div class="brand brand--right">
      <span class="brand__mark"></span>
      <div>
        <div class="brand__name">Maple Junction Property Consultants</div>
        <div class="brand__tag">Experiential Retail And Turn Around Professionals</div>
      </div>
    </div>
    <div class="page-no page-no--right"><span class="page-no__label">PAGE</span><span class="page-no__value">2</span></div>
    <p class="tagline tagline--center">We don't just build your business,&nbsp; We build your community</p>
  </section>

  <section class="slide slide--content-b">
    <svg viewBox="0 0 620 465" aria-hidden="true">
      <path d="M0,359 Q360,470 620,293 V465 H0 Z" fill="var(--green)" opacity="0.7"/>
      <path d="M0,375 Q360,478 620,349 V465 H0 Z" fill="var(--purple)"/>
      <path d="M0,405 Q360,470 620,371 V465 H0 Z" fill="var(--green)"/>
    </svg>
    <div class="brand brand--left">
      <span class="brand__mark"></span>
      <div>
        <div class="brand__name">Maple Junction Property Consultants</div>
        <div class="brand__tag">Experiential Retail And Turn Around Professionals</div>
      </div>
    </div>
    <div class="page-no page-no--left"><span class="page-no__label">PAGE</span><span class="page-no__value">2</span></div>
    <p class="tagline tagline--right">We excel in generating revenue,<br>Enhancing the guest experience and Protecting the brand.</p>
  </section>

</div>
</body>
</html>
```